Snapframe Party Rentals New Business Card*

Need a business card designed for a Photo Booth Hire company.Must look very professional and colorful.A new creative logo would be a bonus. Our current logo is attached on here.

Contact Information for Business Card

Business Name: SNAPFRAME PARTY RENTALS
Contact Person: MARCUS OKAFOR
Mobile: 0491862035
Email: INFO@SNAPFRAMEPARTY.EXAMPLE
Website: WWW.SNAPFRAMEPARTY.EXAMPLE
Facebook: WWW.SOCIALNET.EXAMPLE/SNAPFRAME.PARTY.RENT

Font styles to use
Serif
Sans Serif
Script

Colors

Designer to choose colors to be used in the design.

Requirements
Must have
• Bonus if the colors match our website.

```html
<!DOCTYPE html>
<html lang="en">
<head>
<meta charset="utf-8">
<title>Snapframe Party Rentals – Business Card</title>
<link rel="stylesheet" href="https://fonts.googleapis.com/css2?family=Cinzel:wght@400;700&family=Roboto:wght@400;700&display=swap">
<style>
  :root {
    --backdrop: #3a3a3c;
    --ink: #0b0b0b;
    --paper: #ffffff;
    --text-grey: #555555;
    --mark-grey: #d9d9d9;
  }
  * { box-sizing: border-box; margin: 0; padding: 0; }
  html, body { width: 1200px; height: 960px; overflow: hidden; }
  body { background: var(--backdrop); position: relative; font-family: "Roboto", sans-serif; }

  .card { position: absolute; width: 560px; height: 320px; }

  .card-front { left: 60px; top: 130px; background: var(--ink); color: var(--paper);
    display: flex; flex-direction: column; align-items: center; justify-content: center; }
  .wordmark { font-family: "Cinzel", serif; font-weight: 400; font-size: 34px; letter-spacing: 2px;
    line-height: 1.25; text-align: center; color: var(--paper); }
  .tagline { margin-top: 6px; font-family: "Roboto", sans-serif; font-weight: 700; font-size: 10px;
    letter-spacing: 1px; text-transform: uppercase; color: var(--paper); }

  .card-back { left: 580px; top: 500px; background: var(--paper); overflow: hidden; }
  .mark-area { position: absolute; left: 370px; top: 60px; width: 150px; height: 150px;
    border-radius: 50%; background: var(--mark-grey); }
  .name-ribbon { position: absolute; left: 0; top: 170px; width: 330px; height: 60px; }
  .holder-name { position: absolute; left: 28px; top: 202px; font-weight: 700; font-size: 19px;
    letter-spacing: 0.5px; color: var(--paper); }
  .contact-list { position: absolute; left: 40px; top: 240px; list-style: none; }
  .contact-list li { display: flex; align-items: center; gap: 8px; font-size: 13px;
    color: var(--text-grey); line-height: 18px; }
  .contact-list svg { width: 10px; height: 10px; flex: none; fill: var(--ink); }
</style>
</head>
<body>
  <section class="card card-front">
    <h1 class="wordmark">SNAPFRAME<br>PARTY RENTALS</h1>
    <p class="tagline">Melbourne's most affordable party rental company</p>
  </section>

  <section class="card card-back">
    <div class="mark-area" role="img" aria-label="Brand mark: glasses and moustache emblem"></div>
    <svg class="name-ribbon" viewBox="0 0 330 60" aria-hidden="true">
      <polygon points="0,28 230,28 262,0 330,0 300,28 300,60 0,60" fill="#0b0b0b"/>
    </svg>
    <p class="holder-name">MARCUS OKAFOR</p>
    <ul class="contact-list">
      <li><svg viewBox="0 0 10 10"><path d="M2 0 L4 2.5 L3 3.5 Q4 6 6.5 7 L7.5 6 L10 8 L8.5 10 Q2 9 0 1.5 Z"/></svg>0491862035</li>
      <li><svg viewBox="0 0 10 10"><path d="M0 2 H10 V8 H0 Z M0 2 L5 6 L10 2" /></svg>info@snapframeparty.example</li>
      <li><svg viewBox="0 0 10 10"><circle cx="5" cy="5" r="5"/></svg>www.snapframeparty.example</li>
      <li><svg viewBox="0 0 10 10"><circle cx="5" cy="5" r="5"/></svg>/snapframe.party.rent</li>
    </ul>
  </section>
</body>
</html>
```